Cobalt Homes Web Site Design

improve on the graphic design on our current website
www.cobalthmoes.com.au
wordpress required

Graphic Design

Coding

Coded - Design and coding required

Number of Pages Required

5+ page

```html
<!DOCTYPE html>
<html lang="en">
<head>
<meta charset="utf-8">
<title>Cobalt Homes</title>
<link href="https://fonts.googleapis.com/css2?family=Raleway:wght@400;500;600;700;800&family=Open+Sans:wght@400;600;700&display=swap" rel="stylesheet">
<style>
:root{
  --red:#a3172e;
  --red-dark:#8c1226;
  --grey:#6a6868;
  --charcoal:#3b3737;
  --ink:#222;
  --muted:#666;
  --line:#dcdcdc;
  --black:#151313;
  --topbar:#2a2828;
  --white:#fff;
}
*{margin:0;padding:0;box-sizing:border-box}
html,body{width:1200px;height:3629px;overflow:hidden}
body{font-family:"Open Sans",Arial,sans-serif;color:var(--ink);background:var(--white);font-size:13px;position:relative}
h1,h2,h3,h4{font-family:"Raleway",Arial,sans-serif}
.section{position:absolute;left:0;width:1200px}

/* top bar */
.topbar{top:0;height:29px;background:var(--topbar);color:#cfcfcf;font-size:10px;display:flex;align-items:center;padding:0 162px;gap:28px;letter-spacing:.3px}
.topbar .hours{margin-left:auto}
.topbar svg{vertical-align:-2px;margin-right:6px}

/* header */
.header{top:29px;height:92px;display:flex;align-items:center;padding:0 162px;border-bottom:1px solid #eee}
.brand{display:flex;align-items:center;gap:10px;font-family:"Raleway",sans-serif;font-weight:700;font-size:26px;color:var(--ink)}
.brand .dot{width:30px;height:30px;border-radius:50%;background:var(--red)}
.nav{margin-left:auto;display:flex;gap:34px;font-family:"Raleway",sans-serif;font-size:11.5px;font-weight:600;letter-spacing:.5px}
.nav a{color:var(--ink);text-decoration:none}
.nav a.active{color:var(--red)}
.tools{display:flex;gap:8px;margin-left:34px}
.tools span{width:30px;height:30px;border-radius:50%;display:flex;align-items:center;justify-content:center}
.tools .cart{background:var(--red)}
.tools .search{background:var(--charcoal)}

/* hero */
.hero{top:121px;height:564px}
.hero-photo{position:absolute;inset:0;background:linear-gradient(180deg,#8fa9c4 0%,#c4c9c9 40%,#6b5d4a 70%,#2c3a25 100%)}
.hero-copy{position:absolute;left:0;right:0;top:228px;text-align:center;color:var(--white)}
.hero-copy h1{font-size:40px;font-weight:700;letter-spacing:1px}
.hero-copy p{font-size:15px;font-weight:600;width:480px;margin:12px auto 0;line-height:1.5}
.btn{display:inline-block;background:var(--red);color:var(--white);font-family:"Raleway",sans-serif;font-weight:700;font-size:12px;letter-spacing:.5px;padding:10px 18px;border-radius:2px}
.hero-copy .btn{margin-top:26px}
.dots{display:flex;gap:6px;justify-content:center}
.dots i{width:13px;height:13px;border-radius:50%;background:var(--white);display:block}
.dots i.on{background:transparent;border:2px solid var(--white)}
.hero .dots{position:absolute;bottom:50px;left:0;right:0}

/* services */
.services{top:685px;height:242px;display:flex}
.service{width:400px;height:100%;padding:46px 0 0 48px;color:var(--white)}
.service.red{background:var(--red)}
.service.grey{background:var(--grey)}
.service.dark{background:var(--charcoal)}
.service .head{display:flex;align-items:center;gap:20px}
.service h3{font-size:16px;font-weight:600;line-height:1.5;letter-spacing:.4px}
.service p{font-size:12px;line-height:1.75;margin-top:22px;width:320px}

/* why */
.why{top:927px;height:481px;text-align:center}
.section-title{font-size:22px;font-weight:700;letter-spacing:.6px;color:var(--ink)}
.section-title em{font-style:normal;color:var(--red)}
.why .section-title{margin-top:54px}
.why .intro{width:800px;margin:26px auto 0;font-size:11.5px;line-height:1.7;color:var(--muted)}
.why-photo{position:absolute;left:169px;top:170px;width:252px;height:252px;border-radius:50%;background:linear-gradient(180deg,#b48fb8 0%,#d9a8a0 40%,#5b5e66 70%,#2f3b2a 100%);border:4px solid var(--white);box-shadow:0 0 0 4px var(--red)}
.features{position:absolute;left:515px;top:200px;width:540px;display:grid;grid-template-columns:1fr 1fr;text-align:left}
.feature{padding:0 0 36px 0;width:250px}
.feature:nth-child(2n){padding-left:30px;border-left:1px solid var(--line)}
.feature h4{font-size:17px;font-weight:500;display:flex;align-items:center;gap:12px}
.feature p{font-size:11px;color:var(--muted);line-height:1.7;margin:14px 0 0 0}

/* portfolio */
.portfolio{top:1408px;height:521px;background:var(--charcoal);text-align:center}
.portfolio .section-title{color:var(--white);margin-top:38px}
.filters{display:flex;justify-content:center;gap:6px;margin-top:26px}
.filters span{border:1px solid #bbb;color:var(--white);font-size:10.5px;font-weight:600;padding:6px 10px;letter-spacing:.4px}
.filters span.on{background:var(--red);border-color:var(--red)}
.grid{position:absolute;left:162px;top:153px;width:876px;height:302px;display:grid;grid-template-columns:repeat(4,1fr);grid-template-rows:1fr 1fr;gap:12px}
.tile{background:linear-gradient(180deg,#8db1d6,#c7c9c5 55%,#5c6a4a)}
.tile.tall{grid-row:span 2}
.tile.dusk{background:linear-gradient(180deg,#2e4673,#5a6d94 45%,#b49070 75%,#3b3a3a)}
.tile.warm{background:linear-gradient(180deg,#1f2f52,#6c5e58 55%,#d9965a 80%,#2a2622)}
.tile.day2{background:linear-gradient(180deg,#aac6e3,#e4e2dc 55%,#7c8c6c)}

/* team */
.team{top:1929px;height:532px;text-align:center}
.team .section-title{margin-top:50px}
.members{position:absolute;top:136px;left:0;right:0;display:flex;justify-content:center;gap:102px}
.member{width:222px}
.avatar{width:222px;height:222px;border-radius:50%;background:radial-gradient(circle at 50% 40%,#cfcfcf,#6e6e6e 70%,#333);box-shadow:0 0 0 4px var(--white),0 0 0 7px var(--red)}
.member h3{font-size:14px;font-weight:700;margin-top:30px;letter-spacing:.4px}
.member p{font-size:11px;line-height:1.6;color:var(--muted);margin-top:14px;width:260px;margin-left:-19px}
.member .role{font-family:"Raleway",sans-serif;font-weight:700;color:var(--red);font-size:12px;margin-top:18px}

/* testimonials */
.testimonials{top:2461px;height:366px;background:var(--red);color:var(--white)}
.testimonials .section-title{color:var(--white);text-align:center;margin-top:64px}
.quote-photo{position:absolute;left:160px;top:134px;width:110px;height:110px;border-radius:50%;background:linear-gradient(180deg,#e8e8e8,#6a7384 60%,#2a3040);border:4px solid var(--white)}
.quote{position:absolute;left:290px;top:138px;width:752px;font-size:11px;line-height:1.75;font-style:italic}
.quote .mark{font-family:Georgia,serif;font-size:18px;font-style:normal;margin-right:6px}
.quote cite{display:block;margin-top:12px;font-size:10px;font-style:normal;font-weight:700;letter-spacing:.5px}
.testimonials .dots{position:absolute;left:0;right:0;top:298px}

/* contact */
.contact{top:2827px;height:476px;text-align:center}
.contact .section-title{margin-top:50px}
.contact .intro{width:800px;margin:26px auto 0;font-size:11px;line-height:1.75;color:var(--muted)}
.form{position:absolute;left:162px;top:170px;width:503px;display:grid;grid-template-columns:1fr 1fr;gap:8px 8px;text-align:left}
.field{border:1px solid var(--line);height:32px;font-size:10.5px;padding:8px 8px;color:#444}
.field.wide{grid-column:span 2;height:112px}
.form .btn{position:absolute;left:0;top:226px;padding:10px 22px}
.map{position:absolute;left:692px;top:174px;width:348px;height:206px;background:linear-gradient(135deg,#e7e5df,#d6e3c4 50%,#c9d8b4);border:1px solid var(--line)}

/* footer */
.footer{top:3303px;height:326px;background:var(--black);color:#cfcfcf}
.footer .brand{position:absolute;left:162px;top:42px;color:var(--white);font-size:24px}
.footer .about{position:absolute;left:162px;top:110px;width:290px;font-size:10.5px;line-height:1.75}
.social{position:absolute;left:162px;top:278px;display:flex;gap:8px}
.social i{width:24px;height:24px;border-radius:50%;border:1px solid #888;display:block}
.col{position:absolute;top:88px}
.col h4{color:var(--white);font-size:13px;font-weight:700;letter-spacing:.5px;margin-bottom:14px}
.col li{list-style:none;font-size:9.5px;line-height:2;text-transform:uppercase;letter-spacing:.3px}
.col.menu{left:503px}
.col.services-list{left:656px}
.col.contact-info{left:835px}
.contact-info .row{display:flex;gap:12px;font-size:10px;line-height:1.6;margin-bottom:12px}
.contact-info .row span.ic{flex:none;width:22px;height:22px;border-radius:50%;border:1px solid #999;display:flex;align-items:center;justify-content:center}
.copyright{position:absolute;left:795px;top:282px;font-size:10px}
</style>
</head>
<body>

<div class="section topbar">
  <span><svg width="10" height="8" viewBox="0 0 10 8"><rect x=".5" y=".5" width="9" height="7" fill="none" stroke="#cfcfcf"/><path d="M.5 .5 5 4.5 9.5 .5" fill="none" stroke="#cfcfcf"/></svg>NEED AN ESTIMATE? GET A QUOTE »</span>
  <span><svg width="9" height="9" viewBox="0 0 10 10"><path d="M2 0 4 3 3 4c1 2 2 3 3 3l1-1 3 2-1 2C5 10 0 5 0 1z" fill="#cfcfcf"/></svg>CALL US NOW: 0400 555 172</span>
  <span class="hours"><svg width="9" height="9" viewBox="0 0 10 10"><circle cx="5" cy="5" r="4.3" fill="none" stroke="#cfcfcf"/><path d="M5 2.5V5h2" stroke="#cfcfcf" fill="none"/></svg>Mon – Fri: 7:00 – 15:00 · Sat – Sun: 8:00 – 13:00</span>
</div>

<header class="section header">
  <div class="brand"><span class="dot"></span>Cobalt Homes</div>
  <nav class="nav">
    <a class="active" href="#">HOME</a><a href="#">COMPANY</a><a href="#">EXCELLENCE</a><a href="#">EXPERIENCE</a><a href="#">EXPERTISE</a><a href="#">CONTACT</a>
  </nav>
  <div class="tools">
    <span class="cart"><svg width="12" height="12" viewBox="0 0 12 12"><path d="M1 2h2l1.5 6h6l1-4.5H4" fill="none" stroke="#fff" stroke-width="1.3"/><circle cx="5" cy="10.3" r="1" fill="#fff"/><circle cx="10" cy="10.3" r="1" fill="#fff"/></svg></span>
    <span class="search"><svg width="12" height="12" viewBox="0 0 12 12"><circle cx="5" cy="5" r="3.6" fill="none" stroke="#fff" stroke-width="1.5"/><path d="M7.7 7.7 11 11" stroke="#fff" stroke-width="1.6"/></svg></span>
  </div>
</header>

<section class="section hero">
  <div class="hero-photo" role="img" aria-label="Modern two-storey home with palm trees and a pool at dusk"></div>
  <div class="hero-copy">
    <h1>COBALT HOMES?</h1>
    <p>Lorem ipsum dolor sit amet, consectetur adipiscing elit, sed do eiusmod tempor incididunt ut labore et dolore gnaus.</p>
    <span class="btn">WATCH OUR VIDEO</span>
  </div>
  <div class="dots"><i></i><i class="on"></i><i></i></div>
</section>

<section class="section services">
  <div class="service red">
    <div class="head">
      <svg width="46" height="42" viewBox="0 0 46 42" fill="none" stroke="#fff" stroke-width="2.4"><path d="M3 40h40M6 40V16l17-12 17 12v24"/><rect x="12" y="20" width="6" height="6"/><rect x="28" y="20" width="6" height="6"/><rect x="12" y="30" width="6" height="6"/><rect x="28" y="30" width="6" height="6"/><rect x="20" y="28" width="6" height="12"/></svg>
      <h3>CANBERRA<br>BUILDING SERVICES</h3>
    </div>
    <p>Cobalt Homes is a Canberra based building company focusing on first class residential homes and 100% client satisfaction.</p>
  </div>
  <div class="service grey">
    <div class="head">
      <svg width="40" height="44" viewBox="0 0 40 44" fill="#fff"><path d="M8 16a12 12 0 0 1 24 0z"/><rect x="6" y="16" width="28" height="3"/><circle cx="20" cy="24" r="6"/><path d="M4 44c0-10 7-14 16-14s16 4 16 14z"/></svg>
      <h3>TOP CLASS<br>ARCHITECTS</h3>
    </div>
    <p>Cobalt Homes is a Canberra based building company focusing on first class residential homes and 100% client satisfaction.</p>
  </div>
  <div class="service dark">
    <div class="head">
      <svg width="46" height="46" viewBox="0 0 46 46" fill="none" stroke="#fff" stroke-width="2.4"><path d="M6 44h22M10 44V8h6v36M16 8l26 10M10 8 4 14M38 17v10"/><rect x="34" y="27" width="8" height="6"/><path d="M10 14l6 6M16 20l-6 6M10 26l6 6M16 32l-6 6"/></svg>
      <h3>RELIABLE<br>CONTRACTORS</h3>
    </div>
    <p>Cobalt Homes is a Canberra based building company focusing on first class residential homes and 100% client satisfaction.</p>
  </div>
</section>

<section class="section why">
  <h2 class="section-title">WHY COBALT <em>HOMES?</em></h2>
  <p class="intro">Our vision is to build homes to the highest standards. We're a boutique building company in Canberra, that has built many residential properties. Being in the industry for many years has enabled us to master the art of designing and constructing stylish homes that are not only aesthetically pleasing but also affordable.</p>
  <div class="why-photo" role="img" aria-label="Contemporary single-storey home under a pink evening sky"></div>
  <div class="features">
    <div class="feature">
      <h4><svg width="16" height="16" viewBox="0 0 16 16"><path d="M1 7 15 1 9 15 7 9z" fill="var(--red)"/></svg>Houses we built</h4>
      <p>Sed ut perspiciatis unde omnisreis isa swolu tatem accusa ntiudoloremqlaam lortum.</p>
    </div>
    <div class="feature">
      <h4><svg width="16" height="16" viewBox="0 0 16 16"><circle cx="8" cy="5" r="4" fill="var(--red)"/><path d="M1 16c0-5 3-6 7-6s7 1 7 6z" fill="var(--red)"/></svg>People in Our Team</h4>
      <p>Sed ut perspiciatis unde omnisreis isa swolu tatem accusa ntiudoloremqlaam lortum.</p>
    </div>
    <div class="feature">
      <h4><svg width="14" height="16" viewBox="0 0 14 16"><path d="M7 0 14 3v5c0 4-3 7-7 8-4-1-7-4-7-8V3z" fill="var(--red)"/></svg>Sed utlorem pers?</h4>
      <p>Sed ut perspiciatis unde omnisreis isa swolu tatem accusa ntiudoloremqlaam lortum.</p>
    </div>
    <div class="feature">
      <h4><svg width="16" height="16" viewBox="0 0 16 16"><path d="M1 7h3v8H1zM5 7l3-6c2 0 2 2 1.5 4H15l-1.5 9H5z" fill="var(--red)"/></svg>Sed utlorem pers?</h4>
      <p>Sed ut perspiciatis unde omnisreis isa swolu tatem accusa ntiudoloremqlaam lortum.</p>
    </div>
  </div>
</section>

<section class="section portfolio">
  <h2 class="section-title">OUR PORTFOLIO</h2>
  <div class="filters"><span class="on">ALL</span><span>GALLERY</span><span>BUILDER</span><span>EXTENSIONS</span><span>BATHROOMS</span><span>REFURBISHMENT</span></div>
  <div class="grid">
    <div class="tile" role="img" aria-label="White weatherboard family home"></div>
    <div class="tile tall dusk" role="img" aria-label="Modern home with lit pool at twilight"></div>
    <div class="tile day2" role="img" aria-label="Large suburban house with lawn"></div>
    <div class="tile tall warm" role="img" aria-label="Two-storey home with warm lights at night"></div>
    <div class="tile day2" role="img" aria-label="Grey two-storey home on a sunny day"></div>
    <div class="tile" role="img" aria-label="Family home with front garden"></div>
  </div>
</section>

<section class="section team">
  <h2 class="section-title">OUR <em>TEAM</em></h2>
  <div class="members">
    <div class="member">
      <div class="avatar" role="img" aria-label="Portrait of team member"></div>
      <h3>DANIEL ASHFORD</h3>
      <p>Lorem ipsum dolor sit amet, consectetur adiled do eiusmod tempor incididunt ut labore et doluqall quat enim ad minim veniamconsectetulds.</p>
      <div class="role">CEO &amp; ARCHITECT</div>
    </div>
    <div class="member">
      <div class="avatar" role="img" aria-label="Portrait of team member"></div>
      <h3>DANIEL ASHFORD</h3>
      <p>Lorem ipsum dolor sit amet, consectetur adiled do eiusmod tempor incididunt ut labore et doluqall quat enim ad minim veniamconsectetulds.</p>
      <div class="role">CEO &amp; ARCHITECT</div>
    </div>
    <div class="member">
      <div class="avatar" role="img" aria-label="Portrait of team member"></div>
      <h3>DANIEL ASHFORD</h3>
      <p>Lorem ipsum dolor sit amet, consectetur adiled do eiusmod tempor incididunt ut labore et doluqall quat enim ad minim veniamconsectetulds.</p>
      <div class="role">CEO &amp; ARCHITECT</div>
    </div>
  </div>
</section>

<section class="section testimonials">
  <h2 class="section-title">CLIENT TESTIMONIALS</h2>
  <div class="quote-photo" role="img" aria-label="Photo of client"></div>
  <blockquote class="quote">
    <span class="mark">“</span>At vero eos et accusamus et iusto odio dignissimos ducimus qui blanditiis praesentium voluptatum deleniti atque corrupti quos dolores et quas mol estias excepturi sint occaecati cupiditate non provident, similique sunt in culpa qui officia deserunt mollitia animi, id est laborum et dolorum fuga. Et harum quidem rerum facilis est et expedita distinctio. Nam libero tempore, cum soluta nobis est eligendi optio cumque nihil impedit quo minus id quod maxime placeat facere udem rerum facilis est et expedita distinctioan libero.<span class="mark">”</span>
    <cite>JANE MERROW, CITY NAME</cite>
  </blockquote>
  <div class="dots"><i></i><i class="on"></i><i></i></div>
</section>

<section class="section contact">
  <h2 class="section-title">GET IN <em>TOUCH</em></h2>
  <p class="intro">Sed ut perspiciatis unde omnis iste natus error sit voluptatem accusantium doloremque laudantium, totam rem aperiam, eaque ipsa quae ab illo inventore veritat ut perspiciatis unde omnis iste natus error sit voluptatem accusantium doloremque laudantium, totam rem aperiam, eaque ipsa quae ab illo inventore veri</p>
  <div class="form">
    <div class="field">Name:</div><div class="field">Description:</div>
    <div class="field">Email:</div><div class="field">Call you?:</div>
    <div class="field">Phone:</div><div class="field">Subject:</div>
    <div class="field wide">Message:</div>
    <span class="btn">SUBMIT</span>
  </div>
  <div class="map" role="img" aria-label="Street map showing the office location"></div>
</section>

<footer class="section footer">
  <div class="brand">Cobalt Homes</div>
  <p class="about">Cobalt Homes is a boutique building company based in Canberra ACT. Having been in the construction industry for many years have turned us into experts in the field. For any of your building and construction needs, please don't hesitate to contact us.</p>
  <div class="social"><i></i><i></i><i></i><i></i></div>
  <div class="col menu">
    <h4>MENU</h4>
    <ul><li>Home</li><li>Company</li><li>Excellence</li><li>Experience</li><li>Expertise</li><li>Contact</li></ul>
  </div>
  <div class="col services-list">
    <h4>SERVICES</h4>
    <ul><li>General Builder</li><li>House Extensions</li><li>Refurbishment</li><li>Electricity</li><li>Bathrooms</li><li>Kitchens</li></ul>
  </div>
  <div class="col contact-info">
    <h4>CONTACT US</h4>
    <div class="row"><span class="ic"><svg width="10" height="12" viewBox="0 0 10 12"><path d="M5 12S0 7 0 4.5a5 5 0 0 1 10 0C10 7 5 12 5 12z" fill="#ccc"/><circle cx="5" cy="4.5" r="1.6" fill="#151313"/></svg></span><span>12 Harlow Street, Kingston<br>Canberra, ACT.</span></div>
    <div class="row"><span class="ic"><svg width="10" height="10" viewBox="0 0 10 10"><path d="M2 0 4 3 3 4c1 2 2 3 3 3l1-1 3 2-1 2C5 10 0 5 0 1z" fill="#ccc"/></svg></span><span>Tel: 0400 555 172</span></div>
    <div class="row"><span class="ic"><svg width="10" height="8" viewBox="0 0 10 8"><rect x=".5" y=".5" width="9" height="7" fill="none" stroke="#ccc"/><path d="M.5 .5 5 4.5 9.5 .5" fill="none" stroke="#ccc"/></svg></span><span>E-mail: hello@cobalthomes.com.au<br>Get directions on the map</span></div>
  </div>
  <div class="copyright">© 2016 Cobalthomes. All copyrights are reserved.</div>
</footer>

</body>
</html>
```